Pelkman Agency (http://pa.quorvexstudio.com/)

We are looking for a similar design to what we have, but more professional looking and cleaned up with links and logo that is not so grainy looking. We are an independent insurance agency marketing to personal and commercial clients. We offer all commercial lines markets and all personal lines. We target excavators, landscapers, restaurants, golf courses, contractors. Please look at http://pa.quorvexstudio.com/ which we had designed but do not like it, it will give you an idea of what we are looking for.

Target Market(s)

Commercial and personal insurance. All business products and all personal (homeowners, auto, antique auto, umbrella)

Industry/Entity Type

It Professional

Logo Text

Knowledge Building Your Assurance

Number of Pages Required

5+ page

Colors
000000
848484
0255a3

```html
<!DOCTYPE html>
<html lang="en">
<head>
<meta charset="utf-8">
<title>Pelkman Agency – Personal Insurance</title>
<link rel="stylesheet" href="https://fonts.googleapis.com/css2?family=Open+Sans:wght@300;400;600;700&display=swap">
<style>
:root{
  --blue:#1a7dc9;
  --blue-dark:#0e6fb8;
  --ink:#333;
  --gray:#848484;
  --line:#e4e4e4;
  --thumb:#e6e7e8;
  --foot:#3b3c3f;
  --foot-bar:#333437;
  --foot-text:#c9c9c9;
  --link-blue:#39a5f0;
}
*{box-sizing:border-box;margin:0;padding:0}
html,body{width:1200px;height:1182px;overflow:hidden;background:#fff}
body{font-family:"Open Sans",Arial,sans-serif;color:var(--ink)}
.stage{width:1366px;height:1346px;position:relative;transform:scale(.87848);transform-origin:0 0}
.abs{position:absolute}
a{color:inherit;text-decoration:none}

.topbar{left:0;top:0;width:1366px;height:42px;border-bottom:1px solid #ececec}
.topbar .contact{left:99px;top:14px;font-size:11px;color:#777}
.topbar .contact .mail{font-size:13px;color:#999;margin-left:4px}
.social-top{top:17px;left:1094px;display:flex;gap:27px}
.dot{width:13px;height:13px;border-radius:50%;background:#cfcfcf}
.dot.on{background:var(--blue)}

.header{left:0;top:42px;width:1366px;height:91px;box-shadow:0 8px 14px -8px rgba(0,0,0,.12);background:#fff;z-index:2}
.logo{left:100px;top:26px;font-size:31px;font-weight:400;color:#333;letter-spacing:.2px}
.nav{top:35px;font-size:15px;color:#333}
.nav.active{color:var(--blue)}
.nav-mark{left:655px;top:0;width:137px;height:3px;background:var(--blue)}

.band{left:0;top:133px;width:1366px;height:170px;background:linear-gradient(#f1f1f1,#fff)}
.page-title{left:99px;top:178px;font-size:26px;font-weight:300;color:var(--blue)}
.crumbs{left:343px;top:189px;font-size:12px;color:#666}
.crumbs a{text-decoration:underline}
.crumbs .sep{margin:0 9px}
.rule{left:98px;top:233px;width:1170px;height:1px;background:#ddd}
.rule-mark{left:98px;top:232px;width:103px;height:3px;background:var(--blue)}
.search{left:960px;top:188px;width:271px;height:37px;border:1px solid #ddd;background:#fff;font-size:13px;color:#aaa;padding:10px 9px}
.search-btn{left:1230px;top:188px;width:38px;height:37px;background:var(--blue)}

.heading{left:98px;top:288px;font-size:37px;font-weight:300;color:#333}
.pager{top:294px;width:33px;height:33px;border:1px solid var(--blue);color:var(--blue);font-size:13px;text-align:center;line-height:31px;background:#fff}
.pager.cur{background:var(--blue);color:#fff}

.card{top:366px;width:274px;height:291px;border:1px solid #e2e2e2;text-align:center}
.card .thumb{height:226px;background:var(--thumb)}
.card h3{margin-top:10px;font-size:17px;font-weight:700;color:var(--blue);letter-spacing:.3px}
.card p{font-size:15px;color:var(--gray);margin-top:0}

.footer{left:0;top:829px;width:1366px;height:440px;background:var(--foot);color:var(--foot-text)}
.f-logo{left:96px;top:68px;font-size:31px;color:#fff}
.f-head{top:77px;font-size:15px;font-weight:700;color:#fff}
.f-text{font-size:13px;line-height:22px}
.f-item{font-size:13px;line-height:22px;color:#e6e6e6;padding-left:16px;position:relative}
.f-item:before{content:"";position:absolute;left:1px;top:8px;width:5px;height:5px;border-right:1.5px solid #ddd;border-top:1.5px solid #ddd;transform:rotate(45deg)}
.f-item small{display:block;font-size:11px;color:var(--link-blue);line-height:18px}
.f-item b{font-weight:400;color:#fff}
.f-ico{left:99px}
.news-input{left:976px;top:182px;width:179px;height:30px;background:#e9e9e9;font-size:13px;color:#999;padding:6px 11px}
.news-btn{left:1155px;top:182px;width:88px;height:30px;background:var(--blue);color:#fff;font-size:13px;text-align:center;line-height:30px}
.social-foot{left:976px;top:290px;display:flex;gap:33px}
.social-foot .dot{width:22px;height:22px;background:#5a5b5e}
.social-foot .dot.on{background:var(--blue)}

.bottom{left:0;top:1269px;width:1366px;height:77px;background:var(--foot-bar);color:#d5d5d5;font-size:12px}
.bottom .copy{left:99px;top:30px}
.bottom .fl{top:30px;font-weight:600}
</style>
</head>
<body>
<div class="stage">

  <div class="abs topbar">
    <div class="abs contact">Call Us Today! &nbsp;1-888-4 PELKMN &nbsp;| <span class="mail">admin@pelkmanagency.com</span></div>
    <div class="abs social-top"><span class="dot on"></span><span class="dot"></span><span class="dot"></span><span class="dot"></span><span class="dot"></span></div>
  </div>

  <header class="abs header">
    <div class="abs nav-mark"></div>
    <div class="abs logo">Pelkman Agency</div>
    <a class="abs nav" style="left:581px">Home</a>
    <a class="abs nav active" style="left:653px">Personal Insurance</a>
    <a class="abs nav" style="left:833px">Business Insurance</a>
    <a class="abs nav" style="left:1013px">About Us</a>
    <a class="abs nav" style="left:1121px">Contact Us</a>
    <a class="abs nav" style="left:1229px">More</a>
  </header>

  <div class="abs band"></div>
  <h1 class="abs page-title">Personal Insurance</h1>
  <div class="abs crumbs"><a>Home</a><span class="sep">›</span><a>Personal Insurance</a></div>
  <div class="abs rule"></div>
  <div class="abs rule-mark"></div>
  <div class="abs search">To search enter keyword</div>
  <div class="abs search-btn"><svg width="38" height="37" viewBox="0 0 38 37"><path d="M15 14l4 4.5-4 4.5M20 14l4 4.5-4 4.5" fill="none" stroke="#fff" stroke-width="1.8"/></svg></div>

  <h2 class="abs heading">We Provide</h2>
  <div class="abs pager" style="left:1091px"><svg width="31" height="31" viewBox="0 0 31 31"><path d="M18 10l-5 5.5 5 5.5" fill="none" stroke="currentColor" stroke-width="1.6"/></svg></div>
  <div class="abs pager cur" style="left:1127px">1</div>
  <div class="abs pager" style="left:1163px">2</div>
  <div class="abs pager" style="left:1199px">3</div>
  <div class="abs pager" style="left:1235px"><svg width="31" height="31" viewBox="0 0 31 31"><path d="M13 10l5 5.5-5 5.5" fill="none" stroke="currentColor" stroke-width="1.6"/></svg></div>

  <div class="abs card" style="left:98px"><div class="thumb" role="img" aria-label="Annuity insurance photo"></div><h3>Annuity Insurance</h3><p>Short Description</p></div>
  <div class="abs card" style="left:396px"><div class="thumb" role="img" aria-label="Car insurance photo"></div><h3>Car Insurance</h3><p>Short Description</p></div>
  <div class="abs card" style="left:695px"><div class="thumb" role="img" aria-label="Home insurance photo"></div><h3>Home Insurance</h3><p>Short Description</p></div>
  <div class="abs card" style="left:993px"><div class="thumb" role="img" aria-label="Long term care insurance photo"></div><h3>Long Term Care Insurance</h3><p>Short Description</p></div>

  <footer class="abs footer">
    <div class="abs f-logo">Pelkman Agency</div>
    <div class="abs f-text" style="left:99px;top:131px">Your Slogan Or short Description<br>Goes Here</div>

    <svg class="abs f-ico" style="top:203px" width="12" height="16" viewBox="0 0 12 16"><path d="M6 0a5.5 5.5 0 0 0-5.5 5.5C.5 9.5 6 16 6 16s5.5-6.5 5.5-10.5A5.5 5.5 0 0 0 6 0zm0 7.5a2 2 0 1 1 0-4 2 2 0 0 1 0 4z" fill="#aaa"/></svg>
    <div class="abs f-text" style="left:127px;top:201px">Pelkman Agency<br>PO Box 742<br>15 Harbor Lane<br>Brookfield, NJ 08123</div>
    <svg class="abs f-ico" style="top:293px" width="13" height="13" viewBox="0 0 13 13"><path d="M2.5 0l2.3 2.8-1.4 1.6a8 8 0 0 0 5.2 5.2l1.6-1.4L13 10.5 11.3 13C5 12.6.4 8 0 1.7z" fill="#aaa"/></svg>
    <div class="abs f-text" style="left:127px;top:289px">Phone: (555) 310-4826</div>
    <svg class="abs f-ico" style="top:315px" width="15" height="13" viewBox="0 0 15 13"><path d="M3.5 0h8v3.5h-8zM0 4.5h15v6h-3V13H3v-2.5H0zm4.5 4v3h6v-3z" fill="#aaa"/></svg>
    <div class="abs f-text" style="left:127px;top:311px">Fax: (555) 310-4827</div>
    <svg class="abs f-ico" style="top:360px" width="15" height="11" viewBox="0 0 15 11"><path d="M0 0h15v11H0z" fill="#aaa"/><path d="M0 .5l7.5 6 7.5-6" fill="none" stroke="#3b3c3f" stroke-width="1.3"/></svg>
    <div class="abs f-text" style="left:127px;top:355px">admin@pelkmanagency.com</div>

    <div class="abs f-head" style="left:390px">RECENT POSTS</div>
    <div class="abs f-item" style="left:390px;top:131px">Consecte tur adipiscing elit ut eunt<small>3 days ago</small></div>
    <div class="abs f-item" style="left:390px;top:191px">Fusce vel tempus augue nunc<small>5 days ago</small></div>
    <div class="abs f-item" style="left:390px;top:251px">Lorem nulla, vitae eleifend leo tincidunt<small>7 days ago</small></div>

    <div class="abs f-head" style="left:683px">RECENT TWEETS</div>
    <div class="abs f-item" style="left:683px;top:131px;width:270px">Integer iaculis egestas odio, vel dictum turpis placerat id. Pellentesque semper nisl eget: <b>t.co/Kx4mPq2Lzr</b><small style="margin-top:4px">2 days ago</small></div>
    <div class="abs f-item" style="left:683px;top:251px;width:270px">Curabitur consequat tortor ut eros posu ere rutrum donec metus nisl, dictum vita fermentum: <b>t.co/Kx4mPq2Lzr</b><small style="margin-top:4px">6 days ago</small></div>

    <div class="abs f-head" style="left:976px">NEWSLETTER</div>
    <div class="abs f-text" style="left:977px;top:131px">Get The latest News!</div>
    <div class="abs news-input">Email Address</div>
    <div class="abs news-btn">Subscribe</div>
    <div class="abs f-head" style="left:976px;top:256px">SOCIAL MEDIA</div>
    <div class="abs social-foot"><span class="dot on"></span><span class="dot"></span><span class="dot"></span><span class="dot"></span><span class="dot"></span></div>
  </footer>

  <div class="abs bottom">
    <div class="abs copy">Copyright 2015 Pelkman Agency | All Rights Reserved</div>
    <a class="abs fl" style="left:664px">Home</a>
    <a class="abs fl" style="left:736px">Personal Insurance</a>
    <a class="abs fl" style="left:880px">Business Insurance</a>
    <a class="abs fl" style="left:1024px">Service Center</a>
    <a class="abs fl" style="left:1132px">About Us</a>
    <a class="abs fl" style="left:1204px">Contact Us</a>
  </div>

</div>
</body>
</html>
```